New DL Brochures for Kites Gymnastics Centres

Kites Gymnastics is about to launch its new website and to coincide with this we would like to produce a complete new set of brochures for all of our programs (10 programs)
Kites Gymnastics provides sports coaching for young children in gymnastics lessons as well as conducting holiday programs and birthday parties.
Our company colours are red, gold and black but we are trying to maintain a clean, sharp image so lots of white should be used to highlight our colours.
The brochures should all follow the same template and be clean, fresh, simple and exciting making you want to use our services.
Each brochure should contain 1 or 2 pictures (you decide !) as well as our logo (ideally at the top) with our contact details at the bottom (contact details will be required to be changed for each of our 4 locations)
We have a supply of images which will replace the stock photo supplied for the winning bid.
UPDATE - I will consider postcard type designs which may allow a more diverse range of ideas - this could be very effective way to display the information
Updates
Project Deadline Extended
Reason: I have increased the budget and would like to encourage more designs :)
I am now considering postcard type designs for this project as well as DL sized designs. After looking over a couple of designs it may be possible to do a great "postcard" style design with a great picture and basic info on the front and program info on the back of the postcard
Hi All,
Target Market(s)
Parents of young children
Industry/Entity Type
It Company
Look and feel
Each slider illustrates characteristics of the customer's brand and the style your logo design should communicate.

```html
<!DOCTYPE html>
<html lang="en">
<head>
<meta charset="utf-8">
<title>Kites Gymnastics – Program Postcards</title>
<link href="https://fonts.googleapis.com/css2?family=Arimo:wght@400;700&display=swap" rel="stylesheet">
<style>
  :root {
    --brand-red: #e8453c;
    --brand-gold: #ffe100;
    --star-gold: #f7b500;
    --ink: #1a1a1a;
    --paper: #ffffff;
    --backdrop: #efebe7;
    --wing-light: #f1f1f1;
    --wing-dark: #bdbdbd;
  }
  * { box-sizing: border-box; margin: 0; padding: 0; }
  html, body {
    width: 1200px; height: 900px; overflow: hidden;
    background: var(--backdrop);
    font-family: "Arimo", Arial, sans-serif;
    color: var(--ink);
  }
  .sheet { position: relative; width: 1200px; height: 900px; }

  .card {
    position: absolute;
    width: 540px;
    background: var(--paper);
    box-shadow: 0 4px 14px rgba(0,0,0,0.18);
    overflow: hidden;
  }
  .card--front { height: 390px; top: 40px; }
  .card--back { height: 390px; top: 462px; }
  .card--left { left: 40px; }
  .card--right { left: 620px; }

  /* Front */
  .front-panel { position: absolute; inset: 0; width: 100%; height: 100%; }
  .front-panel polygon { fill: var(--brand-red); }
  .program-title {
    position: absolute; left: 24px; top: 38px;
    color: var(--ink); font-weight: 700; font-size: 21px; line-height: 1.2;
  }
  .highlights {
    position: absolute; left: 24px; list-style: none;
    color: var(--paper); font-size: 14.5px; line-height: 1.3;
  }
  .highlights li { position: relative; padding-left: 24px; margin-bottom: 14px; }
  .highlights svg { position: absolute; left: 0; top: 1px; width: 14px; height: 14px; }
  .highlights svg polygon { fill: var(--brand-gold); }
  .card--left .highlights { top: 100px; width: 200px; }
  .card--right .highlights { top: 112px; width: 190px; }

  .brand-name {
    position: absolute; right: 28px; top: 42px;
    display: flex; align-items: center; gap: 8px;
    color: var(--brand-red); font-weight: 700; font-size: 22px; letter-spacing: 0.2px;
  }
  .brand-name .mark { width: 14px; height: 14px; border-radius: 50%; background: var(--brand-red); }

  .illustration { position: absolute; }
  .illustration--star {
    left: 285px; top: 120px; width: 220px; height: 210px; border-radius: 12px;
    background: radial-gradient(circle at 45% 40%, #ffd23a, var(--star-gold) 70%, #e08a00);
  }
  .illustration--wings {
    left: 300px; top: 140px; width: 180px; height: 150px; border-radius: 12px;
    background: linear-gradient(90deg, var(--wing-light), var(--wing-dark) 50%, var(--wing-light));
  }

  /* Back */
  .program-info {
    position: absolute; left: 0; top: 0; width: 100%; height: 302px;
    background: var(--brand-red);
    color: var(--paper);
    padding: 12px 20px 0;
  }
  .program-info p { margin-bottom: 12px; }
  .card--left .program-info { font-size: 13.5px; line-height: 1.28; }
  .card--right .program-info { font-size: 12.3px; line-height: 1.24; padding-top: 10px; }
  .card--right .program-info p { margin-bottom: 9px; }
  .accent { color: var(--brand-gold); font-weight: 700; }
  .cta { color: var(--ink); font-weight: 700; }
  .cta .accent { color: var(--brand-gold); }
  .card--left .cta-line { margin-top: 14px; font-size: 14px; }

  .contact-band {
    position: absolute; left: 0; bottom: 0; width: 100%; height: 88px;
    background: var(--paper);
    display: flex; justify-content: space-between;
    padding: 12px 20px 0;
    font-size: 12.5px; line-height: 1.3;
  }
  .contact-details .location { color: var(--brand-red); font-weight: 700; }
  .club-tagline { text-align: center; padding-top: 4px; }
  .club-tagline .quote { color: var(--brand-red); font-weight: 700; font-size: 13px; }
  .club-tagline .award { font-weight: 700; }
</style>
</head>
<body>
<main class="sheet">

  <!-- Gymstar front -->
  <section class="card card--front card--left">
    <svg class="front-panel" viewBox="0 0 540 390" preserveAspectRatio="none" aria-hidden="true">
      <polygon points="0,0 300,0 195,390 0,390"/>
    </svg>
    <h2 class="program-title">Gymstar<br>(10-16 years)</h2>
    <ul class="highlights">
      <li><svg viewBox="0 0 24 24"><polygon points="12,1 15,9 23,9 17,14 19,23 12,18 5,23 7,14 1,9 9,9"/></svg>Uses our own unique Levels System</li>
      <li><svg viewBox="0 0 24 24"><polygon points="12,1 15,9 23,9 17,14 19,23 12,18 5,23 7,14 1,9 9,9"/></svg>Keeps children focused on progressing</li>
      <li><svg viewBox="0 0 24 24"><polygon points="12,1 15,9 23,9 17,14 19,23 12,18 5,23 7,14 1,9 9,9"/></svg>Skills include roundoffs, handsprings, flips &amp; somersaults</li>
      <li><svg viewBox="0 0 24 24"><polygon points="12,1 15,9 23,9 17,14 19,23 12,18 5,23 7,14 1,9 9,9"/></svg>Creates amazing self confidence</li>
      <li><svg viewBox="0 0 24 24"><polygon points="12,1 15,9 23,9 17,14 19,23 12,18 5,23 7,14 1,9 9,9"/></svg>Is challenging, SAFE &amp; progressive</li>
    </ul>
    <div class="brand-name"><span class="mark"></span>Kites Gymnastics</div>
    <div class="illustration illustration--star" role="img" aria-label="Large glossy gold star illustration"></div>
  </section>

  <!-- Tumbling & Trampoline front -->
  <section class="card card--front card--right">
    <svg class="front-panel" viewBox="0 0 540 390" preserveAspectRatio="none" aria-hidden="true">
      <polygon points="0,0 300,0 195,390 0,390"/>
    </svg>
    <h2 class="program-title">Tumbling &amp;<br>Trampoline<br>(5-16 years)</h2>
    <ul class="highlights">
      <li><svg viewBox="0 0 24 24"><polygon points="12,1 15,9 23,9 17,14 19,23 12,18 5,23 7,14 1,9 9,9"/></svg>Fly through the air</li>
      <li><svg viewBox="0 0 24 24"><polygon points="12,1 15,9 23,9 17,14 19,23 12,18 5,23 7,14 1,9 9,9"/></svg>Develop great aerial skills</li>
      <li><svg viewBox="0 0 24 24"><polygon points="12,1 15,9 23,9 17,14 19,23 12,18 5,23 7,14 1,9 9,9"/></svg>Skills include roundoffs, handsprings, flips &amp; somersaults</li>
      <li><svg viewBox="0 0 24 24"><polygon points="12,1 15,9 23,9 17,14 19,23 12,18 5,23 7,14 1,9 9,9"/></svg>Is challenging, SAFE &amp; progressive</li>
    </ul>
    <div class="brand-name"><span class="mark"></span>Kites Gymnastics</div>
    <div class="illustration illustration--wings" role="img" aria-label="Pair of silver feathered wings illustration"></div>
  </section>

  <!-- Gymstar back -->
  <section class="card card--back card--left">
    <div class="program-info">
      <p><span class="accent">Gym Star</span> is a Levels based class for 10-16 year olds. Advancing on from the Stars program the Gym Star program provides opportunities for gymnasts to learn more advanced skills.</p>
      <p>Kites has a specially designed Levels system aimed to help the students continue to progress from white level through to black level with a whole range of safe and progressive skills and drills. The early levels develop skills such as rolls, cartwheels, handstands, walkovers, pullovers, back &amp; front drops, students then develop more advanced skills such as roundoffs, flips, somersaults, handsprings, flysprings, kips, giants and more.</p>
      <p>This is a 2 hour/week class. Students may elect to do 2 classes per week. The class also incorporates a range of strength and flexibility development to assist participants to achieve the next level of skills.</p>
      <p class="cta cta-line">Book NOW for a <span class="accent">Free</span> Gym Star Try Out Class</p>
    </div>
    <footer class="contact-band">
      <address class="contact-details" style="font-style:normal">
        <span class="location">Riverton</span> 03 5550 1842<br>
        riverton@kitesgym.example<br>
        27 Marlow St, Elm Park<br>
        1300 KITES GYM (5483 7496)
      </address>
      <div class="club-tagline">
        <div class="quote">“Gymnastics educates children’s bodies”</div>
        <div>Qualified Instructors | Great Facilities | Safe | Fun</div>
        <div class="award">2012 WAG Club of the Year</div>
      </div>
    </footer>
  </section>

  <!-- Tumbling & Trampoline back -->
  <section class="card card--back card--right">
    <div class="program-info">
      <p><span class="accent">The Tumbling &amp; Trampoline</span> program is specifically designed to teach acrobatic skills to all participants in a safe and progressive environment. The program is divided into Beginner, Intermediate and Advanced Classes with students working through our specially designed levels system.</p>
      <p>Students learn lots of basic tumbling &amp; trampolining skills, jumping and twisting as well as developing strength, coordination, spatial awareness and flexibility. When these skills are mastered students progress on to learning flips, somersaults and associated activities.<br>
      Every Kites centre boasts an Olympic sized sprung floor, 2 competition size trampolines and a huge 12m long tumbling trampoline. Students in the classes use all trampolines to learn various skills with classes tailored towards individual needs and skill levels.</p>
      <p>Classes are combined boys and girls and involve a warm up followed by rotations which include trampoline, tumble trampoline, floor, vault and conditioning. Classes involve 1-1½ hours training per week although participants can attend additional sessions if they desire. <span class="cta">Book NOW for a <span class="accent">Free</span> Tumbling &amp; Trampoline Try Out Class</span></p>
    </div>
    <footer class="contact-band">
      <address class="contact-details" style="font-style:normal">
        <span class="location">Riverton</span> 03 5550 1842<br>
        riverton@kitesgym.example<br>
        27 Marlow St, Elm Park<br>
        1300 KITES GYM (5483 7496)
      </address>
      <div class="club-tagline">
        <div class="quote">“Gymnastics educates children’s bodies”</div>
        <div>Qualified Instructors | Great Facilities | Safe | Fun</div>
        <div class="award">2012 WAG Club of the Year</div>
      </div>
    </footer>
  </section>

</main>
</body>
</html>
```